Estate Planning Law Firm opening new branch in Florida

I am an experienced estate planning attorney that recently relocated to Florida. Looking for a banner Ad to place on platforms such as HomeLane, Friendspace and Snapgallery to create publicity for firm and new leads.

```html
<!DOCTYPE html>
<html lang="en">
<head>
<meta charset="utf-8">
<title>Serenova Law Firm – Banner Set</title>
<link href="https://fonts.googleapis.com/css2?family=Cinzel:wght@500;700&family=Roboto:wght@500&family=Roboto+Condensed:wght@600;700&display=swap" rel="stylesheet">
<style>
:root{
  --stage:#a3a3a3;
  --label:#333333;
  --navy:#2b3a4c;
  --teal:#1f7f7c;
  --teal-light:#2f9a97;
  --teal-dark:#0b4a49;
  --white:#ffffff;
  --band-top:#e4ebf4;
  --band-bottom:#ffffff;
  --ink:#2b3a4c;
}
*{margin:0;padding:0;box-sizing:border-box}
html,body{width:1200px;height:982px;overflow:hidden;background:var(--stage)}
.canvas{position:relative;width:1200px;height:982px}
.spec{position:absolute;display:flex;justify-content:space-between;font-family:"Roboto",sans-serif;font-weight:500;font-size:15px;color:var(--label);letter-spacing:.2px}
.banner{position:absolute;background:var(--navy);overflow:hidden}
.banner > svg.art{position:absolute;left:0;top:0}
.icon{display:block;flex:none}
.band{position:absolute;left:0;right:0;bottom:0;background:linear-gradient(var(--band-top),var(--band-bottom))}
.copy{position:absolute;text-align:center;color:var(--white)}
.brand{display:inline-flex;flex-direction:column;align-items:center;font-family:"Cinzel",serif;font-weight:700;line-height:1}
.brand-sub{display:flex;align-items:center;font-family:"Roboto",sans-serif;font-weight:500;letter-spacing:.3px}
.brand-sub::before,.brand-sub::after{content:"";height:1px;background:var(--white);display:block}
.headline{font-family:"Cinzel",serif;font-weight:700;line-height:1.12}
.headline em{font-style:normal;color:var(--teal)}
.lede{font-family:"Roboto Condensed",sans-serif;font-weight:700;text-transform:uppercase;margin-left:auto;margin-right:auto}
.cta{position:absolute;display:flex;align-items:center;justify-content:center;background:linear-gradient(var(--teal-light),var(--teal-dark));color:var(--white);font-family:"Roboto Condensed",sans-serif;font-weight:700;text-transform:uppercase}
.cta-arrow{flex:none;border-radius:50%;background:var(--white);display:flex;align-items:center;justify-content:center}
.call{position:absolute;display:flex;align-items:center;font-family:"Roboto Condensed",sans-serif;font-weight:600;color:var(--ink);white-space:nowrap}

/* HomeLane 1200x628 */
.homelane{left:81px;top:91px;width:511px;height:267px}
.homelane .band{height:32px}
.homelane .copy{left:0;width:325px;top:22px}
.homelane .brand{font-size:22px}
.homelane .brand-sub{font-size:7px;margin-top:2px}
.homelane .brand-sub::before,.homelane .brand-sub::after{width:26px;margin:0 4px}
.homelane .headline{font-size:17.2px;margin-top:22px}
.homelane .lede{font-size:10.5px;line-height:15px;margin-top:8px;width:215px}
.homelane .cta{left:69px;top:207px;width:185px;height:43px;font-size:10.5px;gap:20px}
.homelane .cta-arrow{width:23px;height:23px}
.homelane .call{left:360px;top:244px;font-size:10.5px;gap:10px}

/* Friendspace 851x315 */
.friendspace{left:81px;top:447px;width:362px;height:134px}
.friendspace .band{height:24px;left:160px}
.friendspace .copy{left:170px;width:168px;top:11px}
.friendspace .brand{font-size:14px}
.friendspace .brand-sub{font-size:4.5px;margin-top:1px}
.friendspace .brand-sub::before,.friendspace .brand-sub::after{width:17px;margin:0 2px}
.friendspace .headline{font-size:10.2px;margin-top:8px;line-height:1.15}
.friendspace .lede{font-size:5px;line-height:11px;margin-top:4px}
.friendspace .cta{left:178px;top:113px;width:82px;height:19px;font-size:4.5px;gap:8px}
.friendspace .cta-arrow{width:10px;height:10px}
.friendspace .call{left:275px;top:116px;font-size:5.5px;gap:6px}

/* Snapgallery 1080x1920 */
.snapgallery{left:656px;top:91px;width:460px;height:817px}
.snapgallery .band{height:56px}
.snapgallery .copy{left:0;width:460px;top:500px}
.snapgallery .brand{font-size:25px}
.snapgallery .brand-sub{font-size:8px;margin-top:2px}
.snapgallery .brand-sub::before,.snapgallery .brand-sub::after{width:26px;margin:0 4px}
.snapgallery .headline{font-size:26px;margin-top:13px;line-height:1.12}
.snapgallery .lede{font-size:15px;line-height:20px;margin-top:7px}
.snapgallery .cta{left:138px;top:696px;width:185px;height:43px;font-size:10.5px;gap:20px}
.snapgallery .cta-arrow{width:23px;height:23px}
.snapgallery .call{left:131px;top:775px;font-size:19.5px;gap:18px}
</style>
</head>
<body>
<div class="canvas">

  <div class="spec" style="left:80px;top:66px;width:512px"><span>HOMELANE</span><span>1200 X 628</span></div>
  <div class="spec" style="left:80px;top:419px;width:363px"><span>FRIENDSPACE</span><span>851X 315</span></div>
  <div class="spec" style="left:656px;top:66px;width:460px"><span>SNAPGALLERY</span><span>1080 X 1920</span></div>

  <!-- HomeLane -->
  <section class="banner homelane">
    <svg class="art" width="511" height="235" viewBox="0 0 511 235">
      <defs>
        <linearGradient id="hlRing" x1="0" y1="0" x2="0" y2="1"><stop offset="0" stop-color="#35a3a0"/><stop offset="1" stop-color="#07403f"/></linearGradient>
        <linearGradient id="hlPhoto" x1="0" y1="0" x2="0" y2="1"><stop offset="0" stop-color="#b07a5c"/><stop offset=".45" stop-color="#7a5f55"/><stop offset="1" stop-color="#1e2a3d"/></linearGradient>
      </defs>
      <circle cx="500" cy="118" r="208" fill="url(#hlRing)"/>
      <circle cx="515" cy="112" r="192" fill="url(#hlPhoto)" role="img" aria-label="Photo of the two attorneys smiling in front of a brick wall"/>
    </svg>
    <div class="band"></div>
    <div class="copy">
      <div class="brand">SERENOVA<span class="brand-sub">LAW FIRM, PLLC</span></div>
      <h1 class="headline">ESTATE AND FINANCIAL<br>PLANNING <em>LAW FIRM<br>IN FLORIDA</em></h1>
      <p class="lede">Estate planning &amp; financial planning under one roof Melbourne, FL estate and financial planning</p>
    </div>
    <div class="cta">Book an initial call<span class="cta-arrow"><svg class="icon" width="10" height="10" viewBox="0 0 10 10"><path d="M3.5 1.5 7 5 3.5 8.5" fill="none" stroke="#2b3a4c" stroke-width="1.8"/></svg></span></div>
    <div class="call"><svg class="icon" width="10" height="10" viewBox="0 0 24 24"><path fill="#2b3a4c" d="M6.6 10.8a15.1 15.1 0 0 0 6.6 6.6l2.2-2.2c.3-.3.7-.4 1-.2 1.1.4 2.3.6 3.6.6.6 0 1 .4 1 1V20c0 .6-.4 1-1 1A17 17 0 0 1 3 4c0-.6.4-1 1-1h3.5c.6 0 1 .4 1 1 0 1.3.2 2.5.6 3.6.1.3 0 .7-.2 1z"/></svg><span>CALL : (321) 555-0148</span></div>
  </section>

  <!-- Friendspace -->
  <section class="banner friendspace">
    <div class="band"></div>
    <svg class="art" width="362" height="134" viewBox="0 0 362 134">
      <defs>
        <linearGradient id="fsRing" x1="0" y1="0" x2="0" y2="1"><stop offset="0" stop-color="#35a3a0"/><stop offset="1" stop-color="#07403f"/></linearGradient>
        <linearGradient id="fsPhoto" x1="0" y1="0" x2="0" y2="1"><stop offset="0" stop-color="#b07a5c"/><stop offset=".5" stop-color="#7a5f55"/><stop offset="1" stop-color="#1e2a3d"/></linearGradient>
      </defs>
      <ellipse cx="0" cy="100" rx="162" ry="150" fill="url(#fsRing)"/>
      <ellipse cx="0" cy="100" rx="148" ry="142" fill="url(#fsPhoto)" role="img" aria-label="Photo of the two attorneys smiling in front of a brick wall"/>
    </svg>
    <div class="copy">
      <div class="brand">SERENOVA<span class="brand-sub">LAW FIRM, PLLC</span></div>
      <h2 class="headline">ESTATE AND FINANCIAL<br>PLANNING <em>LAW FIRM<br>IN FLORIDA</em></h2>
      <p class="lede">Estate planning &amp; financial planning under one roof<br>Melbourne, FL estate and financial planning</p>
    </div>
    <div class="cta">Book an initial call<span class="cta-arrow"><svg class="icon" width="6" height="6" viewBox="0 0 10 10"><path d="M3.5 1.5 7 5 3.5 8.5" fill="none" stroke="#2b3a4c" stroke-width="2"/></svg></span></div>
    <div class="call"><svg class="icon" width="5" height="5" viewBox="0 0 24 24"><path fill="#1f7f7c" d="M6.6 10.8a15.1 15.1 0 0 0 6.6 6.6l2.2-2.2c.3-.3.7-.4 1-.2 1.1.4 2.3.6 3.6.6.6 0 1 .4 1 1V20c0 .6-.4 1-1 1A17 17 0 0 1 3 4c0-.6.4-1 1-1h3.5c.6 0 1 .4 1 1 0 1.3.2 2.5.6 3.6.1.3 0 .7-.2 1z"/></svg><span>CALL : (321) 555-0148</span></div>
  </section>

  <!-- Snapgallery -->
  <section class="banner snapgallery">
    <svg class="art" width="460" height="761" viewBox="0 0 460 761">
      <defs>
        <linearGradient id="sgRing" x1="0" y1="0" x2="0" y2="1"><stop offset=".5" stop-color="#2a8d8a"/><stop offset="1" stop-color="#07403f"/></linearGradient>
        <linearGradient id="sgPhoto" x1="0" y1="0" x2="0" y2="1"><stop offset="0" stop-color="#b98466"/><stop offset=".4" stop-color="#8a6a5a"/><stop offset="1" stop-color="#1e2a3d"/></linearGradient>
      </defs>
      <circle cx="230" cy="208" r="265" fill="url(#sgRing)"/>
      <g role="img" aria-label="Photo of the two attorneys smiling in front of a brick wall">
        <rect x="0" y="0" width="460" height="200" fill="url(#sgPhoto)"/>
        <circle cx="230" cy="190" r="262" fill="url(#sgPhoto)"/>
      </g>
    </svg>
    <div class="band"></div>
    <div class="copy">
      <div class="brand">SERENOVA<span class="brand-sub">LAW FIRM, PLLC</span></div>
      <h2 class="headline">ESTATE AND FINANCIAL<br>PLANNING <em>LAW FIRM<br>INFLORIDA</em></h2>
      <p class="lede">Estate planning &amp; financial planning under one roof<br>Melbourne, FL estate and financial planning</p>
    </div>
    <div class="cta">Book an initial call<span class="cta-arrow"><svg class="icon" width="10" height="10" viewBox="0 0 10 10"><path d="M3.5 1.5 7 5 3.5 8.5" fill="none" stroke="#2b3a4c" stroke-width="1.8"/></svg></span></div>
    <div class="call"><svg class="icon" width="15" height="15" viewBox="0 0 24 24"><path fill="#2b3a4c" d="M6.6 10.8a15.1 15.1 0 0 0 6.6 6.6l2.2-2.2c.3-.3.7-.4 1-.2 1.1.4 2.3.6 3.6.6.6 0 1 .4 1 1V20c0 .6-.4 1-1 1A17 17 0 0 1 3 4c0-.6.4-1 1-1h3.5c.6 0 1 .4 1 1 0 1.3.2 2.5.6 3.6.1.3 0 .7-.2 1z"/></svg><span>CALL : (321) 555-0148</span></div>
  </section>

</div>
</body>
</html>
```